LoftVane Enterprises Corp., Contractor Tandem Dump Truck, Skidrow Services and 24/7 QuickRun Services

I need to ensure my LoftVane Enterprises Logo is eye catching on the front side. I would like to emphasize the services we supply on the front with eye catching Contractor Tandem Dump Trucks, Skidrows and also offer 24/7 QuickRun Services
Name: Glen Abernathy (owner /Manager), Address: Box 4 Site 7 RR5 Cochrane Alberta Canada T6K-3B8 - Office: 403-555-0172 Cell: 403-555-0248
email: loftvaneenterprisescochrane@mailbox-example.net, Website: www.loftvaneenterprises-example.com
Would like a nice Matt finish card, now you know why I needed 2 sided cards

```html
<!DOCTYPE html>
<html lang="en">
<head>
<meta charset="utf-8">
<title>LoftVane Enterprises Corp. – Business Card</title>
<link rel="stylesheet" href="https://fonts.googleapis.com/css2?family=Roboto:wght@400;500;700&display=swap">
<style>
  :root {
    --backdrop: #2a2522;
    --brand-orange: #d9842f;
    --card-white: #ffffff;
    --ink: #3a3a3a;
  }
  * { box-sizing: border-box; margin: 0; padding: 0; }
  html, body { width: 1200px; height: 715px; overflow: hidden; }
  body {
    background: var(--backdrop);
    font-family: "Roboto", Arial, sans-serif;
  }
  .canvas {
    position: relative;
    width: 1200px;
    height: 715px;
    display: flex;
    align-items: center;
    justify-content: center;
    gap: 40px;
  }
  .card {
    position: relative;
    width: 545px;
    height: 312px;
    border-radius: 3px;
    box-shadow: 0 10px 26px rgba(0,0,0,0.45);
  }
  /* Front side */
  .card-front {
    background: var(--brand-orange);
    display: flex;
    flex-direction: column;
    align-items: center;
    justify-content: center;
    text-align: center;
    color: var(--card-white);
  }
  .front-wordmark {
    font-size: 30px;
    font-weight: 500;
    letter-spacing: 0.5px;
    line-height: 1.2;
  }
  .front-services {
    margin-top: 12px;
    font-size: 10px;
    font-weight: 500;
    letter-spacing: 1.4px;
    text-transform: uppercase;
  }
  /* Back side */
  .card-back {
    background: var(--card-white);
    display: flex;
    align-items: center;
    padding: 0 22px;
  }
  .back-wordmark {
    width: 190px;
    flex: none;
    text-align: center;
    color: var(--brand-orange);
    font-size: 20px;
    font-weight: 500;
    line-height: 1.25;
  }
  .back-services {
    display: block;
    margin-top: 7px;
    font-size: 7px;
    letter-spacing: 0.8px;
    text-transform: uppercase;
  }
  .divider {
    width: 2px;
    height: 150px;
    flex: none;
    background: var(--brand-orange);
    margin: 0 16px;
  }
  .contact { color: var(--ink); font-size: 12px; line-height: 1.4; }
  .contact-name {
    color: var(--brand-orange);
    font-size: 20px;
    font-weight: 700;
    text-transform: uppercase;
    letter-spacing: 0.3px;
  }
  .contact-role { font-size: 12.5px; margin-bottom: 6px; }
  .contact-address { margin-bottom: 4px; }
  .contact-line { display: flex; align-items: center; gap: 6px; font-size: 11px; white-space: nowrap; }
  .contact-line svg { width: 10px; height: 10px; flex: none; }
</style>
</head>
<body>
<main class="canvas">
  <section class="card card-front" aria-label="Card front">
    <div class="front-wordmark">LoftVane<br>Enterprises Corp.</div>
    <div class="front-services">Tandem Dump Trucks · Skidrows · 24/7 QuickRun</div>
  </section>

  <section class="card card-back" aria-label="Card back">
    <div class="back-wordmark">
      LoftVane Enterprises Corp.
      <span class="back-services">Tandem Dump Trucks · Skidrows · 24/7 QuickRun</span>
    </div>
    <div class="divider"></div>
    <div class="contact">
      <div class="contact-name">Glen Abernathy</div>
      <div class="contact-role">Owner/Manager</div>
      <div class="contact-address">Box 4 Site 7 RR5 Cochrane<br>Alberta Canada T6K-3B8</div>
      <div class="contact-line">
        <svg viewBox="0 0 10 10" aria-hidden="true"><path d="M2 1 L3.6 1 L4.2 3 L3.2 3.8 Q4.2 5.8 6.2 6.8 L7 5.8 L9 6.4 L9 8 Q8.6 9 7.6 9 Q1 8.4 1 2.4 Q1 1 2 1 Z" fill="var(--brand-orange)"/></svg>
        <span>403-555-0172</span>
      </div>
      <div class="contact-line">
        <svg viewBox="0 0 10 10" aria-hidden="true"><rect x="2.5" y="0.5" width="5" height="9" rx="1" fill="none" stroke="var(--brand-orange)" stroke-width="1.2"/><circle cx="5" cy="7.8" r="0.6" fill="var(--brand-orange)"/></svg>
        <span>403-555-0248</span>
      </div>
      <div class="contact-line">
        <svg viewBox="0 0 10 10" aria-hidden="true"><rect x="0.6" y="2" width="8.8" height="6" fill="none" stroke="var(--brand-orange)" stroke-width="1.1"/><path d="M0.8 2.3 L5 5.4 L9.2 2.3" fill="none" stroke="var(--brand-orange)" stroke-width="1.1"/></svg>
        <span>www.loftvaneenterprises-example.com</span>
      </div>
      <div class="contact-line">
        <svg viewBox="0 0 10 10" aria-hidden="true"><circle cx="5" cy="5" r="4.3" fill="none" stroke="var(--brand-orange)" stroke-width="1.1"/><ellipse cx="5" cy="5" rx="1.8" ry="4.3" fill="none" stroke="var(--brand-orange)" stroke-width="0.9"/><path d="M0.8 5 H9.2" stroke="var(--brand-orange)" stroke-width="0.9"/></svg>
        <span>loftvaneenterprisescochrane@mailbox-example.net</span>
      </div>
    </div>
  </section>
</main>
</body>
</html>
```